People Search Directory Needs a Web Design

We need a web design for a new web site called Quillfen People Index. We provide free directory information, such as name, phone, address, and email. We also provide other non-white pages information such as the person's relatives, historical records to help identify the person, and link the data so people can find connections. For example, by clicking on an address that a person lives at, you can find other people who might currently (or previously) have lived at that address.

We have a very basic web page that contains a lot of public records data. The page can look very busy. We need it to be concise, where the white pages type of information is easily identifiable, but people also realize the usefulness of the surrounding data (such as possible relatives, email address, historical phone numbers, etc).

The web page also promotes an annual membership to get more in-depth information on people. These Quillfen People Index include a criminal records check, property records, and other information.

Industry/Entity Type

Property

Requirements
Must have
• Attached is an example design we put together. We want the design to be snazzier, have more information architecture thought put into it, etc.

```html
<!DOCTYPE html>
<html lang="en">
<head>
<meta charset="utf-8">
<title>Quillfen People Index – Marlena K Ostrowe</title>
<link rel="stylesheet" href="https://fonts.googleapis.com/css2?family=Arimo:wght@400;700&display=swap">
<style>
:root{
  --navy:#0d4d73;
  --link:#1d7ab5;
  --heading:#1f83b5;
  --text:#2b2b2b;
  --muted:#8a9aa6;
  --line:#dde3e8;
  --page:#eef1f4;
  --card:#ffffff;
  --pink:#e0246a;
  --pink-dark:#b8174f;
  --green-dark:#4e9417;
  --orange:#f29a45;
  --map-tone:#e9e4dc;
  --aerial-tone:#6b6a55;
}
*{box-sizing:border-box;margin:0;padding:0}
html,body{width:969px;height:1200px;overflow:hidden;background:var(--page);font-family:"Arimo",Arial,sans-serif;color:var(--text)}
.stage{width:900px;height:1115px;transform:scale(1.0767);transform-origin:0 0;position:relative}
a{color:var(--link);text-decoration:none}

/* header */
.masthead{position:absolute;left:0;top:0;width:900px;height:100px;background:linear-gradient(180deg,#1a6f9e 0%,#125a85 100%);border-bottom:1px solid #0b4566}
.brand{position:absolute;left:14px;top:30px;display:flex;align-items:center;gap:10px}
.brand-mark{width:22px;height:22px;background:#ffffff;border-radius:3px}
.brand-name{font-size:24px;font-weight:700;color:#ffffff;letter-spacing:.5px}
.tagline{position:absolute;left:18px;top:71px;font-size:12px;color:#d6ecf7}
.nav{position:absolute;left:555px;top:69px;width:317px;height:31px;background:#0e4f78;border-radius:6px 6px 0 0;display:flex;justify-content:space-around;align-items:center;font-size:13px}
.nav a{color:#9cc5dc}
.nav a.is-current{color:#ffffff;font-weight:700}
.btn-membership{position:absolute;left:738px;top:0;width:146px;height:29px;background:var(--pink);color:#fff;font-size:13px;display:flex;align-items:center;justify-content:center;border-radius:0 0 4px 4px;border:1px solid var(--pink-dark);white-space:nowrap}

.searchbar{position:absolute;left:0;top:100px;width:900px;height:110px;background:linear-gradient(180deg,#3ea6d2 0%,#2a86b7 100%)}
.field{position:absolute;top:28px}
.field label{display:block;font-size:13px;color:#ffffff;margin-bottom:6px}
.field .input{height:31px;background:#fff;border:1px solid #9fc9de;border-radius:2px;font-size:12px;color:#8a8a8a;padding:9px 8px}
.field .select{display:flex;justify-content:space-between;align-items:center}
.btn-search{position:absolute;left:767px;top:47px;width:93px;height:35px;background:linear-gradient(180deg,#ec3c7f,#cf1b5d);border:1px solid var(--pink-dark);border-radius:4px;color:#fff;font-weight:700;font-size:15px;display:flex;align-items:center;justify-content:center}

/* profile card */
.profile{position:absolute;left:33px;top:225px;width:828px;height:815px;background:var(--card);border:1px solid var(--line);border-radius:4px}
.profile-head{position:absolute;left:0;top:0;width:100%;height:36px;border-bottom:1px solid var(--line)}
.profile-name{position:absolute;left:11px;top:13px;font-size:14px;color:var(--link)}
.profile-name .sep{color:#b8c3cb;margin:0 6px}
.profile-name .age{color:var(--muted);font-size:13px}
.report-link{position:absolute;right:13px;top:15px;font-size:11px;color:#1b3e5a}

.facts{position:absolute;left:0;top:37px;width:525px}
.fact{position:relative;height:40px;border-bottom:1px solid #e3e8ec;display:flex;align-items:center;padding-left:54px;font-size:12.5px;background:linear-gradient(90deg,#f3f6f8 0%,#ffffff 80%)}
.fact.tall{height:39px;flex-direction:column;align-items:flex-start;justify-content:center;line-height:14px}
.fact .icon{position:absolute;left:20px;top:50%;transform:translateY(-50%)}
.btn-more{position:absolute;right:0;top:14px;width:59px;height:22px;background:linear-gradient(180deg,#86c940,#5ca321);border:1px solid var(--green-dark);border-radius:3px;color:#fff;font-size:10px;font-weight:700;display:flex;align-items:center;justify-content:center;white-space:nowrap}

.section-title{position:absolute;font-size:14px;font-weight:400;color:var(--heading)}
.section-title .slashes{color:#a8b4bd;font-size:11px;margin-right:18px}
.plain-list{position:absolute;list-style:none;font-size:12px;line-height:17.5px}
.num-list{position:absolute;list-style:none;font-size:12px;line-height:17.5px}
.num-list li span{display:inline-block;width:26px}
.divider{position:absolute;left:0;top:454px;width:525px;border-top:2px solid #e3e8ec}

.map{position:absolute;left:543px;width:270px;border:4px solid #cfdde8;border-radius:3px}
.map-streets{top:50px;height:268px;background:linear-gradient(135deg,var(--map-tone),#f3f0ea 60%,#d9e4ea)}
.map-aerial{top:329px;height:246px;background:linear-gradient(160deg,#7b7a64,var(--aerial-tone) 50%,#8a8777)}

/* promo */
.promo{position:absolute;left:9px;top:630px;width:808px;height:176px;background:#f4f6f8;border:1px solid #d5dde3;border-radius:4px}
.promo-title{position:absolute;left:18px;top:12px;font-size:19px;font-weight:700;color:#33424d;white-space:nowrap}
.promo-title a{color:var(--link)}
.dossier{position:absolute;left:18px;top:38px;width:86px;height:100px;background:linear-gradient(160deg,#f6e7bd,#e1c98b);border-radius:2px}
.perks{position:absolute;list-style:none;font-size:12.5px;color:#33424d}
.perks li{display:flex;align-items:center;gap:8px;height:27.5px;white-space:nowrap}
.btn-green{position:absolute;left:8px;top:145px;width:530px;height:24px;background:linear-gradient(180deg,#84c83f,#5ea423);border:1px solid var(--green-dark);border-radius:3px;color:#fff;font-size:11px;font-weight:700;display:flex;align-items:center;justify-content:center}
.report-box{position:absolute;left:563px;top:6px;width:237px;height:165px;background:#fff}
.report-box h3{position:absolute;left:4px;top:13px;font-size:13px;color:#2b3a44;white-space:nowrap}
.report-box p{position:absolute;left:4px;top:50px;width:230px;font-size:12px;line-height:15px;color:#333}
.btn-pink{position:absolute;left:3px;top:139px;width:234px;height:24px;background:linear-gradient(180deg,#eb3a7c,#cf1b5d);border:1px solid var(--pink-dark);border-radius:3px;color:#fff;font-size:11px;font-weight:700;display:flex;align-items:center;justify-content:center}

/* footer */
.footer-nav{position:absolute;left:32px;top:1051px;display:flex;align-items:center;gap:26px;font-size:11px;color:#3a4a55}
.footer-nav a{color:#3a4a55}
.footer-nav a.is-current{background:linear-gradient(180deg,#84c83f,#5ea423);color:#fff;padding:5px 6px;border-radius:3px;border:1px solid var(--green-dark);margin-right:-2px}
.btn-orange{position:absolute;left:705px;top:1053px;width:156px;height:24px;background:var(--orange);border:1px solid #dd8330;border-radius:3px;color:#fff;font-size:13px;display:flex;align-items:center;justify-content:center;white-space:nowrap}
.copyright{position:absolute;left:37px;top:1086px;font-size:11px;color:#4d5a63}
</style>
</head>
<body>
<div class="stage">

  <header class="masthead">
    <div class="brand"><span class="brand-mark"></span><span class="brand-name">QUILLFEN PEOPLE INDEX</span></div>
    <div class="tagline">- free directory information</div>
    <a class="btn-membership" href="#">Get Annual Membership</a>
    <nav class="nav"><a class="is-current" href="#">Home</a><a href="#">About</a><a href="#">People Directory</a><a href="#">Contact</a></nav>
  </header>

  <section class="searchbar">
    <div class="field" style="left:32px"><label>First Name</label><div class="input" style="width:167px">marlena</div></div>
    <div class="field" style="left:212px"><label>M.I.</label><div class="input" style="width:45px"></div></div>
    <div class="field" style="left:271px"><label>Last Name</label><div class="input" style="width:166px">ostrowe</div></div>
    <div class="field" style="left:451px"><label>City</label><div class="input" style="width:140px"></div></div>
    <div class="field" style="left:606px"><label>State</label><div class="input select" style="width:149px">All States <span style="color:#aaa;font-size:9px">▼</span></div></div>
    <a class="btn-search" href="#">Search</a>
  </section>

  <main class="profile">
    <div class="profile-head">
      <div class="profile-name">Marlena K Ostrowe<span class="sep">///</span><span class="age">Age 45</span></div>
      <a class="report-link" href="#">View Marlena's Background Report &gt;&gt;</a>
    </div>

    <div class="facts">
      <div class="fact">
        <svg class="icon" width="20" height="20" viewBox="0 0 24 24"><path fill="#4a5560" d="M6.6 10.8a15 15 0 0 0 6.6 6.6l2.2-2.2a1 1 0 0 1 1-.25 11.4 11.4 0 0 0 3.6.57 1 1 0 0 1 1 1V20a1 1 0 0 1-1 1A17 17 0 0 1 3 4a1 1 0 0 1 1-1h3.5a1 1 0 0 1 1 1c0 1.25.2 2.45.57 3.57a1 1 0 0 1-.25 1z"/></svg>
        (555) 214-0387
        <a class="btn-more" href="#">More Info</a>
      </div>
      <div class="fact">
        <svg class="icon" width="20" height="20" viewBox="0 0 24 24"><path fill="#4a5560" d="M12 3 2 12h3v8h5v-6h4v6h5v-8h3z"/></svg>
        87 Fenwick St Brannock, NY 14019
      </div>
      <div class="fact tall">
        <svg class="icon" width="20" height="16" viewBox="0 0 24 18"><rect x="1" y="1" width="22" height="16" fill="#4a5560"/><path d="M1 1l11 9 11-9" stroke="#fff" stroke-width="2" fill="none"/></svg>
        <span>mko58@larchmail.net</span><span>doublem@larchmail.net</span>
      </div>
      <div class="fact">
        <svg class="icon" width="30" height="22" viewBox="0 0 30 22" style="left:16px"><circle cx="7" cy="7" r="5" stroke="#4a5560" stroke-width="2.5" fill="none"/><circle cx="23" cy="15" r="5" stroke="#4a5560" stroke-width="2.5" fill="none"/><path d="M11 9l8 4" stroke="#4a5560" stroke-width="2"/></svg>
        <span>Check Nationwide Criminal Records For <a href="#">Marlena K Ostrowe &gt;&gt;</a></span>
      </div>
      <div class="fact">
        <svg class="icon" width="20" height="20" viewBox="0 0 24 24"><circle cx="14" cy="9" r="6" stroke="#4a5560" stroke-width="2.5" fill="none"/><path d="M10 13l-7 7" stroke="#4a5560" stroke-width="3" stroke-linecap="round"/></svg>
        <span>Advanced Background Report on <a href="#">Marlena K Ostrowe &gt;&gt;</a></span>
      </div>
    </div>

    <h2 class="section-title" style="left:10px;top:246px"><span class="slashes">///</span>Possible Relatives:</h2>
    <ul class="plain-list" style="left:36px;top:286px">
      <li>Edwin Farrell Ostrowe</li><li>Harold W Ostrowe Sr</li><li>Corwin J Ostrowe</li><li>Nella M Ostrowe</li><li>Rosalind E Ostrowe</li><li>Ivy D Ostrowe</li><li>Edwin K Ostrowe</li><li>Tobias Arthur Ostrowe</li><li>Marisol D Ostrowe</li>
    </ul>

    <h2 class="section-title" style="left:267px;top:246px"><span class="slashes">///</span>Previous Phone Numbers:</h2>
    <ol class="num-list" style="left:268px;top:286px">
      <li><span>1.</span>(555) 214-0387</li><li><span>2.</span>(555) 318-0387</li><li><span>3.</span>(555) 463-2917</li><li><span>4.</span>(555) 967-4410</li>
    </ol>

    <div class="divider"></div>

    <h2 class="section-title" style="left:10px;top:473px"><span class="slashes">///</span>Previous Addresses:</h2>
    <ol class="num-list" style="left:9px;top:513px">
      <li><span>1.</span>31 Aldous St, Brannock, NY 14013</li>
      <li><span>2.</span>453 Wren St #4, Brannock, NY 14017</li>
      <li><span>3.</span>57 Tamsin Pl, Brannock, NY 14018</li>
      <li><span>4.</span>178 Corbel Ave, Brannock, NY 14019</li>
      <li><span>5.</span>50 Hollin St, Brannock, NY 14011</li>
      <li><span>6.</span>None, Brannock, NY 14018</li>
    </ol>

    <div class="map map-streets" role="img" aria-label="Street map marking the current address"></div>
    <div class="map map-aerial" role="img" aria-label="Aerial view of the current address"></div>

    <section class="promo">
      <h2 class="promo-title">Want more in-depth information on <a href="#">Marlena K Ostrowe</a> ?</h2>
      <div class="dossier" role="img" aria-label="Illustration of a personal records folder"></div>
      <ul class="perks" style="left:124px;top:48px">
        <li><svg width="24" height="20" viewBox="0 0 24 20"><path d="M2 11l6 6L22 2" stroke="#5ea423" stroke-width="4" fill="none" stroke-linecap="round"/></svg>Name and AKAs</li>
        <li><svg width="24" height="20" viewBox="0 0 24 20"><path d="M2 11l6 6L22 2" stroke="#5ea423" stroke-width="4" fill="none" stroke-linecap="round"/></svg>Up to 40-year address history</li>
        <li><svg width="24" height="20" viewBox="0 0 24 20"><path d="M2 11l6 6L22 2" stroke="#5ea423" stroke-width="4" fill="none" stroke-linecap="round"/></svg>Date of birth</li>
      </ul>
      <ul class="perks" style="left:368px;top:48px">
        <li><svg width="24" height="20" viewBox="0 0 24 20"><path d="M2 11l6 6L22 2" stroke="#5ea423" stroke-width="4" fill="none" stroke-linecap="round"/></svg>Evictions &amp; bankruptcies</li>
        <li><svg width="24" height="20" viewBox="0 0 24 20"><path d="M2 11l6 6L22 2" stroke="#5ea423" stroke-width="4" fill="none" stroke-linecap="round"/></svg>Property records</li>
        <li><svg width="24" height="20" viewBox="0 0 24 20"><path d="M2 11l6 6L22 2" stroke="#5ea423" stroke-width="4" fill="none" stroke-linecap="round"/></svg>Criminal records check</li>
      </ul>
      <a class="btn-green" href="#">Get Advanced Background Report</a>
      <div class="report-box">
        <h3>What's in your background report ?</h3>
        <p>See what records are publicly available in your background report. Also, check out the public records in reports for your friends and family.</p>
        <a class="btn-pink" href="#">Check My Background Report</a>
      </div>
    </section>
  </main>

  <footer>
    <nav class="footer-nav"><a class="is-current" href="#">Home</a><a href="#">About</a><a href="#">People Directory</a><a href="#">FAQs</a><a href="#">Privacy</a><a href="#">Terms</a><a href="#">Contact</a></nav>
    <a class="btn-orange" href="#">Get Annual Membership</a>
    <div class="copyright">Copyright © 2012 QuillfenPeopleIndex.com</div>
  </footer>

</div>
</body>
</html>
```